Copperleaf Motorized Shade Business Card

Hello, we've had our logo made. Now we are looking for a clean and cool looking business card. One side can just be the logo with any design elements that might look good with it. The other side will be Name, Phone Number and Email. There will not be an address on the card.

```html
<!DOCTYPE html>
<html lang="en">
<head>
<meta charset="utf-8">
<title>Copperleaf Motorized Shade – Business Card</title>
<link rel="stylesheet" href="https://fonts.googleapis.com/css2?family=Oswald:wght@500;600&family=Montserrat:wght@400;500&display=swap">
<style>
  :root {
    --backdrop: #1b3366;
    --card-navy: #24407f;
    --card-navy-deep: #1e3670;
    --accent-gold: #e2b72f;
    --accent-gold-soft: rgba(226, 183, 47, 0.55);
    --accent-gold-clear: rgba(226, 183, 47, 0);
    --accent-sky: #2b9fe3;
    --text-white: #f2f4f8;
  }
  * { box-sizing: border-box; margin: 0; padding: 0; }
  html, body {
    width: 1200px;
    height: 800px;
    overflow: hidden;
  }
  body {
    background: var(--backdrop);
    font-family: "Montserrat", sans-serif;
    color: var(--text-white);
    position: relative;
  }
  .card {
    position: absolute;
    top: 250px;
    width: 525px;
    height: 300px;
    background: linear-gradient(135deg, var(--card-navy-deep), var(--card-navy));
    overflow: hidden;
    box-shadow: 0 12px 30px rgba(5, 14, 40, 0.45);
  }
  .card--contact { left: 50px; }
  .card--brand { left: 625px; }

  .card__accent {
    position: absolute;
    top: 0;
    right: 0;
    height: 100%;
    background: linear-gradient(to right, var(--accent-gold-clear), var(--accent-gold-soft));
  }
  .card--contact .card__accent { width: 50px; }
  .card--brand .card__accent { width: 120px; }

  .contact {
    position: absolute;
    left: 44px;
    top: 92px;
  }
  .contact__name {
    font-family: "Oswald", sans-serif;
    font-weight: 600;
    font-size: 38px;
    line-height: 1;
    letter-spacing: 0.5px;
    color: var(--text-white);
  }
  .contact__role {
    font-weight: 500;
    font-size: 13.5px;
    letter-spacing: 1.2px;
    color: var(--accent-sky);
    margin-top: 3px;
  }
  .contact__list {
    list-style: none;
    margin-top: 20px;
  }
  .contact__item {
    display: flex;
    align-items: center;
    gap: 14px;
    font-size: 11.5px;
    margin-bottom: 11px;
  }
  .contact__icon {
    width: 12px;
    height: 12px;
    fill: var(--accent-sky);
  }

  .card__divider {
    position: absolute;
    left: 255px;
    top: 68px;
    width: 1px;
    height: 192px;
    background: var(--accent-sky);
    opacity: 0.8;
  }

  .brand-name {
    position: absolute;
    display: flex;
    align-items: center;
    gap: 8px;
  }
  .brand-name__mark {
    width: 13px;
    height: 13px;
    background: var(--accent-sky);
  }
  .brand-name__text {
    font-family: "Oswald", sans-serif;
    font-weight: 500;
    color: var(--text-white);
    text-transform: uppercase;
    line-height: 1.05;
    letter-spacing: 0.5px;
  }
  .card--contact .brand-name { left: 286px; top: 124px; }
  .card--contact .brand-name__text { font-size: 15px; }
  .card--brand .brand-name {
    left: 50%;
    top: 50%;
    transform: translate(-50%, -50%);
    gap: 12px;
  }
  .card--brand .brand-name__mark { width: 20px; height: 20px; }
  .card--brand .brand-name__text { font-size: 27px; }
</style>
</head>
<body>

  <section class="card card--contact" aria-label="Business card, contact side">
    <div class="card__accent" role="img" aria-label="Gold accent strokes along the right edge"></div>

    <div class="contact">
      <h1 class="contact__name">NAME HERE</h1>
      <p class="contact__role">ACCOUNT MANAGER</p>
      <ul class="contact__list">
        <li class="contact__item">
          <svg class="contact__icon" viewBox="0 0 24 24" aria-hidden="true"><path d="M6.6 10.8a15.1 15.1 0 0 0 6.6 6.6l2.2-2.2a1 1 0 0 1 1-.25 11.4 11.4 0 0 0 3.6.57 1 1 0 0 1 1 1V20a1 1 0 0 1-1 1A17 17 0 0 1 3 4a1 1 0 0 1 1-1h3.5a1 1 0 0 1 1 1c0 1.25.2 2.45.57 3.57a1 1 0 0 1-.25 1z"/></svg>
          <span>+00 999 999 999</span>
        </li>
        <li class="contact__item">
          <svg class="contact__icon" viewBox="0 0 24 24" aria-hidden="true"><path d="M2 5h20v14H2z M3.5 6.5 12 12.5l8.5-6z" fill-rule="evenodd"/></svg>
          <span>news@yourcompany.com</span>
        </li>
      </ul>
    </div>

    <div class="card__divider"></div>

    <div class="brand-name">
      <span class="brand-name__mark"></span>
      <span class="brand-name__text">Copperleaf<br>Motorized Shade</span>
    </div>
  </section>

  <section class="card card--brand" aria-label="Business card, brand side">
    <div class="card__accent" role="img" aria-label="Gold accent strokes along the right edge"></div>

    <div class="brand-name">
      <span class="brand-name__mark"></span>
      <span class="brand-name__text">Copperleaf<br>Motorized Shade</span>
    </div>
  </section>

</body>
</html>
```